Marketplace Web Re-design overhaul @quarrynest

Hi,
We are currently in production with a website that is getting some mixed feedback about visual appeal and usability. We are using a responsive design and need to stay true to the logo colours and other marketing collateral we have in place. I will provide a brochure with the colour palate we use for some guidance. If you can please help us design something fresh and modern to communicate the essence of our company. The brochure will be a good summary of what we do and who we are targeting as customers. Our current website can be found at www.quarrynest.com. If there is any questions, please let me know.

Target Market(s)

Contractors and Corporate Companies

Industry/Entity Type

Information Technology

Number of Pages Required

4 page

Requirements
Must have
• Must have a complete new visual look, including
• 1. Images
• 2. Background colour scheme overhaul (not black)
• 3. re-design of the layout but keep to similar page breakdowns
Nice to have
• Some of the pages are a bit wordy, happy to have suggestions on how to reduce.
• Would be great if we can integrate the Plumb.ON! blog page to the Quarrynest page?
• This is some feedback a fellow UX designer provided to improve our CRO
• First off when you land on the home page, who is your audience? Are you everything to everyone? Even after watching the video (https://www.vidmarrow.net/watch?v=q7RtPe3LwZ0), I do not know what markets you service or who this app will be for.
• Your main headline and paragraph above the fold I find unnecessarily wordy and an overuse of 'buzzwords' . Perhaps you could look at appealing to the lowest common denominator and make it very simple and put it all into a simple sentence.
• The main hero image to the right of the headline offers no emotional pull at all. I'm assuming it's just a screenshot of your dashboard? Personally, I would be looking at using a person's image in that space.
• Also in this space, increase the size of your 'register' button. On the topic of your register button, you have it in different colours. Green in header, and red in content. Make it the same colour, and don't use that colour again on the site. That colour is to become your call to action (CTA) colour. Understandably you'll have three different colours for the account type, and again, don't use these colours anywhere else on the site.
• The registration area where the three account types are where you choose which one suits you, it's extremely busy with background images and heavy use of text. If you were my client, I would be advising you to ditch the bg image (including the Zelo shot), keeping the text, making the register icons much bigger. Perhaps instead of bg images, use a solid colour for each (green, orange, red). I'm highly confident this change will make a massive difference in your sign up rate.
Should not have
• Please keep to the fonts used on the original website
• Keep to the colour provided on the company brochure for guidance.

```html
<!DOCTYPE html>
<html lang="en">
<head>
<meta charset="utf-8">
<title>Quarrynest — Available, quality talent on demand</title>
<link href="https://fonts.googleapis.com/css2?family=Roboto:wght@300;400;500;700;900&display=swap" rel="stylesheet">
<style>
:root{
  --green:#2fb24a;
  --green-dark:#24963c;
  --orange:#f58a23;
  --red:#e2452f;
  --ink:#2b2e33;
  --muted:#7b8086;
  --light:#f1f2f3;
  --line:#e1e3e5;
  --slate:#3a4049;
  --slate-dark:#2c3138;
  --footer:#33373d;
  --white:#ffffff;
}
*{box-sizing:border-box;margin:0;padding:0}
html,body{width:1200px;height:4212px;overflow:hidden}
body{font-family:'Roboto',Arial,sans-serif;color:var(--ink);background:var(--white);position:relative}
section,header,footer{position:absolute;left:0;width:1200px}
.btn{display:inline-block;background:var(--green);color:var(--white);font-size:14px;font-weight:500;padding:12px 26px;border-radius:3px}
.btn--orange{background:var(--orange)}
.section-title{text-align:center;font-size:30px;font-weight:700;color:var(--ink);letter-spacing:.5px}
.section-sub{text-align:center;font-size:13px;color:var(--muted);margin-top:6px}
.ph{display:block}

/* header */
.site-header{top:0;height:60px;background:var(--white);border-bottom:1px solid var(--line)}
.brand{position:absolute;left:56px;top:16px;display:flex;align-items:center;gap:10px;font-size:24px;font-weight:700;color:var(--green)}
.brand-dot{width:22px;height:22px;border-radius:50%;background:var(--orange)}
.nav{position:absolute;right:60px;top:0;height:60px;display:flex;align-items:center;gap:30px;font-size:13px;font-weight:500;color:var(--ink);text-transform:uppercase}
.nav .active{color:var(--green)}
.nav .login{background:var(--orange);color:var(--white);padding:9px 18px;border-radius:3px}

/* hero */
.hero{top:60px;height:600px;background:linear-gradient(110deg,#2a3642 0%,#3f4e5c 45%,#5a6977 70%,#36424e 100%)}
.hero-photo{position:absolute;left:560px;top:0;width:640px;height:600px;background:radial-gradient(circle at 55% 45%,#7a8896 0%,#4b5966 45%,rgba(54,66,78,0) 75%)}
.hero-copy{position:absolute;left:100px;top:170px;width:520px;color:var(--white)}
.hero-copy h1{font-size:46px;font-weight:900;line-height:1.15;text-transform:uppercase}
.hero-copy p{font-size:14px;line-height:1.6;color:#d5dbe0;margin:22px 0 28px;width:450px}
.hero-arrow{position:absolute;top:280px;width:40px;height:40px;border-radius:50%;background:rgba(255,255,255,.15)}
.hero-arrow.left{left:22px}.hero-arrow.right{right:22px}

/* features */
.features{top:660px;height:470px;background:var(--light);display:flex;justify-content:center;gap:40px;padding-top:80px}
.feature{width:320px;height:290px;background:var(--white);border:1px solid var(--line);text-align:center;padding:0 28px;position:relative}
.feature-icon{width:90px;height:90px;border-radius:50%;background:var(--green);margin:-45px auto 0;display:flex;align-items:center;justify-content:center}
.feature h3{font-size:20px;font-weight:700;margin:30px 0 14px;text-transform:uppercase}
.feature p{font-size:12px;line-height:1.7;color:var(--muted)}
.feature .more{display:block;margin-top:14px;font-size:11px;font-weight:700;color:var(--green);text-transform:uppercase}

/* welcome */
.welcome{top:1130px;height:470px;background:var(--white)}
.welcome-copy{position:absolute;left:100px;top:90px;width:480px}
.welcome-copy h2{font-size:32px;font-weight:700;text-transform:uppercase}
.welcome-copy p{font-size:13px;line-height:1.7;color:var(--muted);margin-top:22px}
.welcome-copy .btn{margin-top:30px}
.welcome-photo{position:absolute;left:620px;top:80px;width:480px;height:300px;background:linear-gradient(135deg,#c9d4dc,#e8ecef 50%,#c3ccd3)}

/* audiences */
.audiences{top:1600px;height:400px;background:linear-gradient(120deg,#3d434b,#555c65 50%,#3a4048)}
.audience{position:absolute;top:70px;width:460px;color:var(--white)}
.audience.contractor{left:100px}.audience.company{left:690px}
.audience h3{font-size:24px;font-weight:400}
.contractor h3{color:var(--green)}.company h3{color:var(--orange)}
.audience h4{font-size:18px;font-weight:500;margin:16px 0 18px}
.audience ul{list-style:none}
.audience li{font-size:12px;color:#d4d8dc;margin-bottom:12px;padding-left:22px;position:relative}
.audience li::before{content:"";position:absolute;left:0;top:2px;width:10px;height:10px;border-radius:50%}
.contractor li::before{background:var(--green)}.company li::before{background:var(--orange)}
.audience .btn{margin-top:12px}

/* video */
.video{top:2000px;height:380px;background:linear-gradient(180deg,#eceeef,#dfe2e4)}
.video-frame{position:absolute;left:360px;top:60px;width:480px;height:260px;background:radial-gradient(circle,#ffffff 0%,#e4e6e8 70%)}
.play{position:absolute;left:570px;top:160px;width:60px;height:60px;border-radius:50%;background:rgba(40,44,50,.8)}

/* blog */
.blog{top:2380px;height:580px;background:var(--white);padding-top:60px}
.posts{display:flex;justify-content:center;gap:30px;margin-top:40px}
.post{width:310px}
.post-image{height:200px;background:linear-gradient(135deg,#c6d0d8,#e9edf0);position:relative}
.post-date{position:absolute;left:20px;top:-6px;width:44px;height:50px;background:var(--green);color:var(--white);font-size:11px;font-weight:700;text-align:center;padding-top:10px;line-height:1.3}
.post h3{font-size:20px;font-weight:700;line-height:1.25;margin:18px 0 10px}
.post p{font-size:12px;line-height:1.6;color:var(--muted)}
.post .btn{margin-top:14px;padding:9px 18px;font-size:12px}

/* team */
.team{top:2960px;height:410px;background:var(--slate);padding-top:50px}
.team .section-title{color:var(--white)}
.team .section-sub{color:#b4bac0}
.members{display:flex;justify-content:center;gap:70px;margin-top:44px}
.member{width:150px;text-align:center;color:var(--white)}
.member-photo{width:110px;height:110px;border-radius:50%;margin:0 auto;background:linear-gradient(135deg,#8a939c,#c4cbd1);border:4px solid #4d545d}
.member h4{font-size:12px;font-weight:700;margin-top:16px;text-transform:uppercase}
.member span{display:block;font-size:11px;color:#b4bac0;margin-top:4px}

/* partners */
.partners{top:3370px;height:250px;background:var(--white);padding-top:50px}
.partner-row{display:flex;justify-content:center;align-items:center;gap:110px;margin-top:50px;position:relative}
.partner{display:flex;align-items:center;gap:10px;font-size:26px;font-weight:700;color:var(--slate)}
.partner i{width:30px;height:30px;display:block}
.p1 i{background:var(--red)}.p2 i{border-radius:50%;background:#2d5aa0}.p3 i{background:var(--green)}
.partner-arrow{position:absolute;top:4px;width:26px;height:26px}
.partner-arrow.left{left:90px}.partner-arrow.right{right:90px}

/* newsletter */
.newsletter{top:3620px;height:160px;background:var(--light);padding-top:34px}
.newsletter .section-title{font-size:24px}
.signup{display:flex;justify-content:center;gap:20px;margin-top:24px}
.field{width:340px;height:40px;background:var(--white);border:1px solid var(--line);font-size:12px;color:#a2a7ac;padding:12px 14px}
.signup .btn{height:40px;padding:12px 30px}

/* footer */
.site-footer{top:3780px;height:350px;background:var(--footer);color:#c2c7cc;padding:50px 100px 0;display:flex;gap:60px}
.fcol h5{font-size:13px;font-weight:700;color:var(--white);text-transform:uppercase;margin-bottom:18px}
.fcol p,.fcol li{font-size:11px;line-height:1.8}
.fcol ul{list-style:none}
.col-about{width:300px}.col-links{width:150px}.col-social{width:250px}.col-contact{width:240px}
.fbrand{display:flex;align-items:center;gap:8px;font-size:18px;font-weight:700;color:var(--green);margin-bottom:12px}
.fbrand i{width:14px;height:14px;border-radius:50%;background:var(--orange);display:block}
.socials{display:flex;gap:8px}
.socials i{width:26px;height:26px;border-radius:50%;display:block}
.contact-line{display:flex;gap:8px;align-items:flex-start}
.contact-line svg{flex:none;margin-top:3px}
.bottom-bar{top:4130px;height:82px;background:var(--green);color:var(--white);font-size:11px;display:flex;align-items:center;justify-content:center}
</style>
</head>
<body>

<header class="site-header">
  <div class="brand"><span class="brand-dot"></span>Quarrynest</div>
  <nav class="nav">
    <span class="active">Home</span><span>How it works</span><span>About us</span><span>Our partners</span><span>F.A.Q.</span><span>Blog</span><span class="login">Login</span>
  </nav>
</header>

<section class="hero">
  <div class="hero-photo ph" role="img" aria-label="Businessman cupping his hands around a network of people icons"></div>
  <span class="hero-arrow left"></span><span class="hero-arrow right"></span>
  <div class="hero-copy">
    <h1>Available, quality talent on demand!</h1>
    <p>Quarrynest helps professional contractors and companies find each other faster, matching skills to projects and connecting the right people at the right time.</p>
    <span class="btn">Get Free Trial</span>
  </div>
</section>

<section class="features">
  <div class="feature">
    <div class="feature-icon"><svg width="40" height="40" viewBox="0 0 40 40" fill="none" stroke="#fff" stroke-width="3"><path d="M8 21l8 8 16-17"/></svg></div>
    <h3>Skills Match</h3>
    <p>Quarrynest compares your skills with project needs, so contractors and companies meet the right match in moments instead of weeks.</p>
    <span class="more">Read more ›</span>
  </div>
  <div class="feature">
    <div class="feature-icon"><svg width="40" height="40" viewBox="0 0 40 40" fill="none" stroke="#fff" stroke-width="3"><rect x="7" y="9" width="26" height="24" rx="2"/><path d="M7 16h26M14 5v7M26 5v7"/></svg></div>
    <h3>Calendar</h3>
    <p>Keep your availability up to date so companies can book you for the days you choose and plan their projects with confidence.</p>
    <span class="more">Read more ›</span>
  </div>
  <div class="feature">
    <div class="feature-icon"><svg width="40" height="40" viewBox="0 0 40 40" fill="none" stroke="#fff" stroke-width="3"><path d="M20 36s11-11 11-20a11 11 0 0 0-22 0c0 9 11 20 11 20z"/><circle cx="20" cy="16" r="4"/></svg></div>
    <h3>Locations</h3>
    <p>Find talent close to your site or search across regions, with location filters that show who can start work near you.</p>
    <span class="more">Read more ›</span>
  </div>
</section>

<section class="welcome">
  <div class="welcome-copy">
    <h2>Welcome to Quarrynest</h2>
    <p>Quarrynest is a unique marketplace connecting contractors with companies, a platform to connect in real time by matching the available talent. Through intuitive search companies can instantly find the skilled professionals they need.</p>
    <p>This is an invaluable tool for companies finding the right people at the right time and at low cost.</p>
    <span class="btn">Read More</span>
  </div>
  <div class="welcome-photo ph" role="img" aria-label="Group photo of smiling professionals"></div>
</section>

<section class="audiences">
  <div class="audience contractor">
    <h3>I'm a Contractor</h3>
    <h4>If you are looking for work</h4>
    <ul>
      <li>Increase exposure by enabling real-time</li>
      <li>Choice of work based on profile matching</li>
      <li>Increase earning potential by dealing directly with companies</li>
    </ul>
    <span class="btn">Join For Free</span>
  </div>
  <div class="audience company">
    <h3>I'm a Company</h3>
    <h4>If you are looking for people</h4>
    <ul>
      <li>Save time by browsing qualified talent in specific availability</li>
      <li>Eliminate needless agent fees and access to active resources</li>
      <li>Negotiate rates directly with the contractor</li>
    </ul>
    <span class="btn btn--orange">Join For Free</span>
  </div>
</section>

<section class="video">
  <div class="video-frame ph" role="img" aria-label="Explainer video still: sketched man at a desk with a No Work sign"></div>
  <svg class="play" viewBox="0 0 60 60"><circle cx="30" cy="30" r="30" fill="rgba(40,44,50,.8)"/><path d="M24 18l18 12-18 12z" fill="#fff"/></svg>
</section>

<section class="blog">
  <h2 class="section-title">OUR BLOG</h2>
  <p class="section-sub">Latest from blog</p>
  <div class="posts">
    <article class="post">
      <div class="post-image ph" role="img" aria-label="Candidates waiting for an interview"><span class="post-date">12<br>JAN</span></div>
      <h3>The Best Tech Skills to List on Your Resume</h3>
      <p>Learning the tech skills hiring teams look for first will help your profile stand out.</p>
      <span class="btn">Read More</span>
    </article>
    <article class="post">
      <div class="post-image ph" role="img" aria-label="Woman in front of a world map"><span class="post-date">08<br>JAN</span></div>
      <h3>The top five in-demand cloud skills for 2016</h3>
      <p>Cloud roles keep growing; these five skills lead the market this year.</p>
      <span class="btn">Read More</span>
    </article>
    <article class="post">
      <div class="post-image ph" role="img" aria-label="Team of young professionals"><span class="post-date">02<br>JAN</span></div>
      <h3>20 hot IT skills that will get you a raise</h3>
      <p>IT professionals with these skills are earning more in every sector right now.</p>
      <span class="btn">Read More</span>
    </article>
  </div>
</section>

<section class="team">
  <h2 class="section-title">THE QUARRYNEST TEAM</h2>
  <p class="section-sub">Stay connected with us</p>
  <div class="members">
    <div class="member"><div class="member-photo ph" role="img" aria-label="Team member portrait"></div><h4>Delia Marchetti</h4><span>CEO &amp; Founder</span></div>
    <div class="member"><div class="member-photo ph" role="img" aria-label="Team member portrait"></div><h4>Owen Brackley</h4><span>CTO &amp; Founder</span></div>
    <div class="member"><div class="member-photo ph" role="img" aria-label="Team member portrait"></div><h4>Rhys Tolland</h4><span>Head of Sales</span></div>
    <div class="member"><div class="member-photo ph" role="img" aria-label="Team member portrait"></div><h4>Ivan Petrosk</h4><span>Product Lead</span></div>
    <div class="member"><div class="member-photo ph" role="img" aria-label="Team member portrait"></div><h4>Samir Haddon</h4><span>Lead Developer</span></div>
  </div>
</section>

<section class="partners">
  <h2 class="section-title">OUR STRATEGIC PARTNERS</h2>
  <div class="partner-row">
    <svg class="partner-arrow left" viewBox="0 0 26 26" fill="none" stroke="#9aa0a6" stroke-width="2"><path d="M16 5l-8 8 8 8"/></svg>
    <div class="partner p1"><i></i>Tallowmere</div>
    <div class="partner p2"><i></i>Fennick Group</div>
    <div class="partner p3"><i></i>Plainly</div>
    <svg class="partner-arrow right" viewBox="0 0 26 26" fill="none" stroke="#9aa0a6" stroke-width="2"><path d="M10 5l8 8-8 8"/></svg>
  </div>
</section>

<section class="newsletter">
  <h2 class="section-title">SUBSCRIBE TO OUR NEWSLETTER</h2>
  <div class="signup">
    <span class="field">Enter your name</span>
    <span class="field">Enter your email</span>
    <span class="btn">Subscribe Now</span>
  </div>
</section>

<footer class="site-footer">
  <div class="fcol col-about">
    <h5>About us</h5>
    <div class="fbrand"><i></i>Quarrynest</div>
    <p>Quarrynest is a marketplace that connects skilled contractors with companies looking for talent, offering real-time availability, direct rates and simple booking for everyone.</p>
  </div>
  <div class="fcol col-links">
    <h5>Quick links</h5>
    <ul><li>Home</li><li>How it works</li><li>About us</li><li>Our partners</li><li>F.A.Q.</li><li>Blog</li></ul>
  </div>
  <div class="fcol col-social">
    <h5>Join us on</h5>
    <div class="socials"><i style="background:#3b5998"></i><i style="background:#1da1f2"></i><i style="background:#dd4b39"></i><i style="background:#0077b5"></i><i style="background:#f58a23"></i><i style="background:#cc2127"></i></div>
  </div>
  <div class="fcol col-contact">
    <h5>Contact us</h5>
    <p class="contact-line"><svg width="10" height="12" viewBox="0 0 10 12"><path d="M5 12S0 7 0 4.5a5 5 0 0 1 10 0C10 7 5 12 5 12z" fill="#2fb24a"/></svg>Office: Quarrynest<br>42 Alder Lane, Northvale 3100</p>
    <p class="contact-line"><svg width="10" height="12" viewBox="0 0 10 12"><rect width="10" height="12" rx="2" fill="#2fb24a"/></svg>Mobile: 0400 123 456</p>
    <p class="contact-line"><svg width="10" height="12" viewBox="0 0 10 12"><rect width="10" height="12" rx="2" fill="#2fb24a"/></svg>Tel: (03) 9000 4821</p>
    <p class="contact-line"><svg width="10" height="12" viewBox="0 0 10 12"><rect y="2" width="10" height="8" fill="#2fb24a"/></svg>hello@quarrynest.com</p>
  </div>
</footer>
<div class="bottom-bar" style="position:absolute;left:0;width:1200px">Copyright © 2016 Quarrynest. All rights reserved. | Privacy Policy</div>

</body>
</html>
```